Photography business - business card design quick turn around

Create a business card design for me please. I actually need the final design back before the end of Sunday 13th May 7pm GMT. Sorry for the short notice.

Photoshop artwork template uploaded with artwork guidelines including printer profiles and other mandatory specifications. Only one side of the business card is required as the other side will be an image.

The design is required as an unflattened PSD file so that I can edit the text if I need to.

My brand colours are white and the teal you see in the logo. Occasionally I also use a dark grey on my website (I don't mind the shade of grey as appreciate grey on teal would be a different grey, to the grey I use on white on the website, so just use a shade of grey that matches). Font can be as the font for the logo or if you prefer I am open to another sans serif, easily legible font. Ideally font size will be 12+.Please do not use capital letters for text. I prefer everything to be lower case, if possible.

Thank you.

Nell

Target Market(s)

Other business owners who may refer me and families

Industry/Entity Type

Photographer

Contact Information for Business Card

Silver Kettle Photography Logo
Sub text: family portraiture, captured with love

Contact information, ideally using simple icons to represent email / website / facebook / instagram / pinterest

email: nell@silverkettlephotography.co.uk
website: silverkettlephotography.co.uk
facebook: @silverkettlephotography
pinterest: pinterest.com/silverkettlepho
instagram: @silverkettle_photography
mobile/telephone: 07931462097

If there is too much text then please drop the instagram and pinterest information.

Font styles to use
Sans Serif

Colors
33b8a4

Requirements
Must have
• Logo
• Contact details as listed above
• sub text
Nice to have
• Instagram and Pinterest contact details
• Nice to have icons to represent website / phone / facebook etc followered by the handle where relevant

```html
<!DOCTYPE html>
<html lang="en">
<head>
<meta charset="utf-8">
<title>Silver Kettle Photography – business card</title>
<link href="https://fonts.googleapis.com/css2?family=Questrial&display=swap" rel="stylesheet">
<style>
  :root {
    --backdrop: #2f2f31;
    --card-grey: #4a4a4c;
    --teal: #1fd0b8;
    --text-light: #f2f2f2;
    --tagline: #d9d9d9;
  }
  * { box-sizing: border-box; margin: 0; padding: 0; }
  html, body {
    width: 1200px;
    height: 1000px;
    overflow: hidden;
    background: var(--backdrop);
    font-family: "Questrial", "Century Gothic", sans-serif;
  }
  .stage {
    width: 1200px;
    height: 1000px;
    display: flex;
    align-items: center;
    justify-content: center;
  }
  .business-card {
    position: relative;
    width: 900px;
    height: 520px;
    background: var(--card-grey);
    border-radius: 30px;
    overflow: hidden;
  }
  .accent-band {
    position: absolute;
    left: 0; top: 0; bottom: 0;
    width: 56px;
    background: var(--teal);
  }
  .brand {
    position: absolute;
    left: 110px;
    top: 62px;
  }
  .brand-name {
    display: flex;
    align-items: center;
    gap: 18px;
    color: var(--teal);
    font-size: 40px;
    letter-spacing: 0.5px;
    text-transform: uppercase;
    line-height: 1;
  }
  .brand-mark {
    width: 46px;
    height: 46px;
    border: 4px solid var(--teal);
    border-radius: 50%;
    flex: none;
  }
  .tagline {
    margin-top: 18px;
    color: var(--tagline);
    font-size: 24px;
    letter-spacing: 3px;
  }
  .contact-list {
    position: absolute;
    left: 110px;
    top: 232px;
    list-style: none;
  }
  .contact-item {
    display: flex;
    align-items: center;
    gap: 14px;
    color: var(--text-light);
    font-size: 23px;
    height: 38px;
  }
  .contact-icon {
    width: 24px;
    height: 24px;
    border-radius: 50%;
    background: var(--teal);
    flex: none;
    display: flex;
    align-items: center;
    justify-content: center;
  }
  .contact-icon svg { width: 14px; height: 14px; }
</style>
</head>
<body>
<main class="stage">
  <section class="business-card">
    <div class="accent-band"></div>

    <header class="brand">
      <div class="brand-name"><span class="brand-mark"></span>Silver Kettle Photography</div>
      <p class="tagline">family portraiture, captured with love</p>
    </header>

    <ul class="contact-list">
      <li class="contact-item">
        <span class="contact-icon">
          <svg viewBox="0 0 16 16"><path d="M4 1.5l2.2 3-1.3 1.6c.8 1.8 2.2 3.2 4 4l1.6-1.3 3 2.2-1.2 2.4C7.5 13.2 2.8 8.5 1.6 3.6z" fill="#4a4a4c"/></svg>
        </span>07931462097
      </li>
      <li class="contact-item">
        <span class="contact-icon">
          <svg viewBox="0 0 16 16"><rect x="2" y="4" width="12" height="8" rx="1" fill="none" stroke="#4a4a4c" stroke-width="1.6"/><path d="M2.5 4.5L8 9l5.5-4.5" fill="none" stroke="#4a4a4c" stroke-width="1.6"/></svg>
        </span>nell@silverkettlephotography.co.uk
      </li>
      <li class="contact-item">
        <span class="contact-icon">
          <svg viewBox="0 0 16 16"><circle cx="8" cy="8" r="6" fill="none" stroke="#4a4a4c" stroke-width="1.4"/><path d="M2 8h12M8 2c-2.5 3-2.5 9 0 12M8 2c2.5 3 2.5 9 0 12" fill="none" stroke="#4a4a4c" stroke-width="1.2"/></svg>
        </span>silverkettlephotography.co.uk
      </li>
      <li class="contact-item">
        <span class="contact-icon"></span>@silverkettlephotography
      </li>
      <li class="contact-item">
        <span class="contact-icon"></span>@silverkettlepho
      </li>
      <li class="contact-item">
        <span class="contact-icon"></span>@silverkettle_photography
      </li>
    </ul>
  </section>
</main>
</body>
</html>
```